Property Management Company looking for a high-end business card, letterhead and envelope design.

We provide high-end / boutique property management for real estate investors or individuals looking for someone to manage their portfolio. we are looking for a cohesive high-end design for our business cards, letterhead and envelopes.

Target Market(s)

Real Estate Investors

Industry/Entity Type

Real Estate

Requirements
Must have
• business card, letterhead and envelope design - logo attached

```html
<!DOCTYPE html>
<html lang="en">
<head>
<meta charset="utf-8">
<title>Halden Property Management — Business Card</title>
<link rel="stylesheet" href="https://fonts.googleapis.com/css2?family=Manrope:wght@300;400;500;600;700&display=swap">
<style>
  :root {
    --brand-blue: #0b4689;
    --brand-blue-deep: #083a73;
    --brand-blue-light: #1a5596;
    --paper: #f4f4f2;
    --ink-gray: #8a8d91;
    --backdrop: #c9cacb;
    --white: #ffffff;
  }
  * { box-sizing: border-box; margin: 0; padding: 0; }
  html, body {
    width: 1200px; height: 900px; overflow: hidden;
    background: var(--backdrop);
    font-family: "Manrope", sans-serif;
  }
  .sheet {
    width: 1200px; height: 900px;
    display: flex; flex-direction: column;
    align-items: center; justify-content: center;
    gap: 40px;
  }
  .card {
    position: relative;
    width: 680px; height: 389px;
    overflow: hidden;
    box-shadow: 0 6px 18px rgba(0, 0, 0, 0.18);
  }

  /* Front */
  .card--front { background: var(--paper); }
  .card__stripe {
    position: absolute; left: 0; top: 0; bottom: 0;
    width: 18px; background: var(--brand-blue);
  }
  .wordmark {
    position: absolute; left: 66px; top: 60px;
    color: var(--brand-blue);
  }
  .wordmark__name {
    font-size: 44px; font-weight: 600;
    letter-spacing: 0.16em; line-height: 1;
  }
  .wordmark__tagline {
    margin-top: 8px;
    font-size: 14px; font-weight: 600;
    letter-spacing: 0.27em; line-height: 1;
  }
  .person {
    position: absolute; left: 66px; top: 160px;
    display: flex; flex-direction: column;
  }
  .person__line {
    display: flex; align-items: flex-end; gap: 14px;
  }
  .person__name {
    color: var(--brand-blue);
    font-size: 22px; font-weight: 700; line-height: 1.1;
    white-space: nowrap;
  }
  .rule {
    width: 400px; height: 1.5px;
    margin-bottom: 5px;
    background: var(--brand-blue);
  }
  .person__title {
    margin-top: 4px;
    color: var(--ink-gray);
    font-size: 14px; font-weight: 400;
    text-transform: uppercase;
  }
  .contact {
    position: absolute; left: 66px; top: 246px;
    color: var(--ink-gray);
    font-size: 16px; line-height: 1.45;
  }
  .contact__label {
    color: var(--brand-blue);
    font-size: 11px; font-weight: 700;
    text-transform: uppercase; margin-left: 4px;
  }
  .contact__email { margin-top: 22px; }
  .office {
    position: absolute; left: 400px; top: 212px;
    color: var(--ink-gray);
    font-size: 16px; line-height: 1.45;
  }
  .office__web {
    margin-top: 26px;
    color: var(--brand-blue);
    font-weight: 500; letter-spacing: 0.12em;
  }

  /* Back */
  .card--back { background: var(--brand-blue); }
  .card__pattern {
    position: absolute; inset: 0;
    background:
      radial-gradient(ellipse at 30% 20%, rgba(255, 255, 255, 0.06), transparent 60%),
      linear-gradient(135deg, var(--brand-blue-light) 0%, var(--brand-blue) 50%, var(--brand-blue-deep) 100%);
  }
  .wordmark--reverse {
    left: 50%; top: 50%;
    transform: translate(-50%, -50%);
    color: var(--white);
  }
</style>
</head>
<body>
  <main class="sheet">
    <section class="card card--front" aria-label="Business card front">
      <div class="card__stripe"></div>
      <div class="wordmark">
        <div class="wordmark__name">HALDEN</div>
        <div class="wordmark__tagline">PROPERTY MANAGEMENT</div>
      </div>
      <div class="person">
        <div class="person__line">
          <div class="person__name">Lorin Vasquez</div>
          <div class="rule"></div>
        </div>
        <div class="person__title">Creative Director</div>
      </div>
      <div class="contact">
        <div>555.014.2200<span class="contact__label">Office</span></div>
        <div>555.014.7381<span class="contact__label">Mobile</span></div>
        <div class="contact__email">info@haldenpm.com</div>
      </div>
      <div class="office">
        <div>18 Harbor Row, 9th Floor</div>
        <div>Brookfield, NY 10990</div>
        <div class="office__web">haldenpm.com</div>
      </div>
    </section>

    <section class="card card--back" aria-label="Business card back">
      <div class="card__pattern" role="img" aria-label="Embossed tone-on-tone repeating brand pattern on deep blue textured paper"></div>
      <div class="wordmark wordmark--reverse">
        <div class="wordmark__name">HALDEN</div>
        <div class="wordmark__tagline">PROPERTY MANAGEMENT</div>
      </div>
    </section>
  </main>
</body>
</html>
```